Steady at Heart: Renew Your Team Through the 6 Habits of Balance

I'm looking for a design that is clean, like the book "Look Sideways" by Milo Brecken. The book is about the principles of organic farming so I am looking for a color scheme that fits that image.
https://www.pagelantern.example/Look-Sideways-Value-Seeing-Other-ebook/dp/Q47K520ZTR/ref=sr_1_3?crid=58XQ2PL07ZV4M&keywords=milo+brecken&qid=1638739111&s=books&sprefix=milo+%2Cstripbooks%2C371&sr=1-3

I don't want a dark color scheme. I prefer a white or cream book with a bold font.

This book is a good example of what I am looking for:

https://www.pagelantern.example/Lamp-Small-Notes-Painting-Days/dp/0912736458/ref=rtpb_2/731-5529043-4417082?pd_rd_w=mq8z3&pf_rd_p=21c9e047-385b-4f7d-a1c2-6e30b8d7f914&pf_rd_r=KP3T8QZ2207LM4NX1VA5&pd_rd_r=e63a1f20-7c4d-4a91-b5e8-09f2d1c7a6e3&pd_rd_wg=3kR2x&pd_rd_i=0912736458&psc=1

Target Market(s)

CEOs and business owners who want to increase the trust in their brands

Industry/Entity Type

Management and Leadership

Colors
00AB8E
00BBA5
67D7C9
C6EFE9
E9F9F6
59FF00
82FF00
B8FF75
E3FFCB
F4FFEA
FFF300
FFF600
FEFA6F
FFFEC7
FFFEE8
FFC000
F8CF3A
FAE287
FDF2CF
FEFAEE

Requirements
Must have
• Author's name is: Harold Vesterby
Nice to have
• I have indicated some books that I like. I would be good to have a simple image such as an apple core or the earth's core or some other image of "core" but not absolutely necessary.
Should not have
• I don't want it to have a dark cover or be too heavy

```html
<!DOCTYPE html>
<html lang="en">
<head>
<meta charset="utf-8">
<title>Steady at Heart — Harold Vesterby</title>
<link rel="stylesheet" href="https://fonts.googleapis.com/css2?family=Bebas+Neue&family=Montserrat:wght@700&family=Questrial&display=swap">
<style>
  :root {
    --page: #ffffff;
    --title-green: #88dc78;
    --frame-top: #f8c064;
    --frame-bottom: #a5d15c;
    --art-leaf: #8ddc7c;
    --art-flesh: #dfe2cc;
    --art-line: #a9dcd6;
  }
  html, body {
    margin: 0;
    padding: 0;
    width: 1200px;
    height: 1200px;
    overflow: hidden;
    background: var(--page);
  }
  .canvas {
    position: relative;
    width: 1200px;
    height: 1200px;
    background: var(--page);
  }
  .cover-frame {
    position: absolute;
    left: 269px;
    top: 105px;
    width: 662px;
    height: 990px;
    box-sizing: border-box;
    border-radius: 4px;
    padding: 4px;
    background: linear-gradient(180deg, var(--frame-top), var(--frame-bottom));
  }
  .cover-frame::after {
    content: "";
    position: absolute;
    inset: 4px;
    background: var(--page);
    border-radius: 2px;
  }
  .cover-type {
    position: absolute;
    left: 0;
    top: 0;
    width: 1200px;
    height: 1200px;
  }
  .title-main {
    font-family: "Bebas Neue", sans-serif;
    fill: var(--title-green);
  }
  .title-second {
    font-family: "Montserrat", sans-serif;
    font-weight: 700;
    fill: var(--title-green);
  }
  .subtitle, .author-name {
    font-family: "Questrial", sans-serif;
    fill: var(--title-green);
  }
  .rule {
    stroke: var(--title-green);
    stroke-width: 1.2;
  }
  .core-artwork {
    position: absolute;
    left: 331px;
    top: 567px;
    width: 559px;
    height: 260px;
    border-radius: 24px;
    background:
      linear-gradient(180deg, transparent 82%, var(--art-line) 82%, var(--art-line) 88%, transparent 88%),
      radial-gradient(ellipse at 50% 40%, var(--art-flesh) 0%, var(--art-leaf) 70%, rgba(255,255,255,0) 100%);
    opacity: 0.75;
  }
</style>
</head>
<body>
<main class="canvas">
  <div class="cover-frame"></div>

  <div class="core-artwork" role="img" aria-label="Hand-drawn illustration of three green apple cores resting above a loose teal scribbled ground line"></div>

  <svg class="cover-type" viewBox="0 0 1200 1200" xmlns="http://www.w3.org/2000/svg">
    <text class="title-main" x="381" y="355" font-size="214" textLength="438" lengthAdjust="spacingAndGlyphs">STEADY</text>
    <text class="title-second" x="380" y="417" font-size="72" textLength="441" lengthAdjust="spacingAndGlyphs">AT HEART</text>
    <line class="rule" x1="380" y1="432" x2="820" y2="432"/>
    <text class="subtitle" x="375" y="465" font-size="31" textLength="452" lengthAdjust="spacingAndGlyphs">RENEW YOUR TEAM THROUGH</text>
    <text class="subtitle" x="400" y="493" font-size="31" textLength="401" lengthAdjust="spacingAndGlyphs">THE 6 HABITS OF BALANCE</text>
    <line class="rule" x1="478" y1="989" x2="737" y2="989"/>
    <text class="author-name" x="450" y="1029" font-size="38" textLength="308" lengthAdjust="spacingAndGlyphs">HAROLD VESTERBY</text>
  </svg>
</main>
</body>
</html>
```